Business Card Design Project for New Home Builder

Double sided card,
Larger logo on 1 side with small quote, Its not just a house, Its your Home, across the bottom. Matt Red base, White logo, black quote??

other side, ,
Its your Home LHS. Smaller logo RHS with.
Details below.

"neuropolitical Rg" Logo Font

Dennis Orford

PO Box 8437 Mildura VIC 3502
Mobile 0427 318865 / Phone 03 50718 962 / Fax 03 50718 415
email DennisO@tbvbuild.net.au
Vic Building Practitioner DB-U 8174 Vic Commercial Builder CB-U 5093
NSW Contractor Reg 37086C

Target Market(s)

New Home Buyers

Industry/Entity Type

Business

Requirements
Must have
• Sharp detail, Red Black & White colourings.
Should not have
• Any new colours

```html
<!DOCTYPE html>
<html lang="en">
<head>
<meta charset="utf-8">
<title>Tallbrook Homes – Business Card</title>
<link rel="stylesheet" href="https://fonts.googleapis.com/css2?family=EB+Garamond:ital,wght@0,400;0,500;1,400&display=swap">
<style>
  :root {
    --red: #e8202a;
    --red-deep: #d11a23;
    --white: #ffffff;
    --paper: #f1efef;
    --ink: #2a2a2a;
    --grey: #8a8a8a;
    --backdrop: #5d5f63;
  }
  * { box-sizing: border-box; margin: 0; padding: 0; }
  html, body { width: 1200px; height: 720px; overflow: hidden; }
  body {
    background: var(--backdrop);
    font-family: "EB Garamond", Georgia, serif;
    display: flex;
    align-items: center;
    justify-content: center;
    gap: 40px;
  }
  .card {
    position: relative;
    width: 540px;
    height: 310px;
    overflow: hidden;
    box-shadow: 0 8px 24px rgba(0,0,0,.35);
  }

  /* Front */
  .card--front { background: var(--red); }
  .card--front .brand {
    position: absolute;
    top: 88px; left: 0; right: 0;
    display: flex; align-items: center; justify-content: center; gap: 12px;
    color: var(--white);
    font-size: 40px; font-weight: 500; letter-spacing: 3px;
  }
  .brand__mark {
    width: 14px; height: 14px; background: currentColor; flex: none;
  }
  .card--front .quote-band {
    position: absolute;
    left: 0; right: 0; top: 218px; height: 34px;
    background: var(--white);
    display: flex; align-items: center; justify-content: flex-end;
    padding-right: 40px;
    font-style: italic; font-size: 15px; color: var(--ink);
  }

  /* Back */
  .card--back { background: var(--paper); color: var(--ink); }
  .card--back .base-band {
    position: absolute; left: 0; right: 0; bottom: 0; height: 34px;
    background: var(--red);
  }
  .credentials {
    position: absolute; top: 44px; left: 30px;
    font-size: 13px; line-height: 1.25;
  }
  .credentials__row { display: flex; gap: 6px; align-items: flex-start; }
  .credentials__list { list-style: none; }
  .credentials .address { color: var(--red); margin-top: 10px; }
  .identity {
    position: absolute; top: 36px; right: 30px;
    text-align: left;
  }
  .card--back .brand {
    display: flex; align-items: center; gap: 8px;
    color: var(--ink); font-size: 22px; font-weight: 500; letter-spacing: 1.5px;
  }
  .card--back .brand__mark { width: 9px; height: 9px; background: var(--red); }
  .identity .name {
    margin-top: 10px; color: var(--red); font-size: 21px; letter-spacing: 1px;
  }
  .identity .role {
    color: var(--grey); font-size: 11px; letter-spacing: 1.5px; margin-top: -2px;
  }
  .contacts {
    position: absolute; top: 160px; left: 300px;
    list-style: none; font-size: 13px; line-height: 1.3;
  }
  .contacts li { display: flex; align-items: center; gap: 7px; }
  .icon { width: 11px; height: 11px; flex: none; fill: var(--red); }
</style>
</head>
<body>

  <section class="card card--front" aria-label="Card front">
    <div class="brand"><span class="brand__mark"></span>TALLBROOK HOMES</div>
    <p class="quote-band">Its not just a house, Its your Home</p>
  </section>

  <section class="card card--back" aria-label="Card back">
    <div class="credentials">
      <div class="credentials__row">
        <svg class="icon" viewBox="0 0 12 12" aria-hidden="true"><path d="M6 1 L11.5 6 H10 V11 H7.3 V8 H4.7 V11 H2 V6 H.5 Z"/></svg>
        <ul class="credentials__list">
          <li>Vic Building Practitioner DB-U 8174</li>
          <li>Vic Commercial Builder CB-U 5093</li>
          <li>NSW Contractor Reg 37086C</li>
        </ul>
      </div>
      <p class="address">PO Box 8437 Mildura VIC 3502</p>
    </div>

    <div class="identity">
      <div class="brand"><span class="brand__mark"></span>TALLBROOK HOMES</div>
      <p class="name">DENNIS ORFORD</p>
      <p class="role">NEUROPOLITICAL RG</p>
    </div>

    <ul class="contacts">
      <li><svg class="icon" viewBox="0 0 12 12" aria-hidden="true"><rect x="3" y="0.5" width="6" height="11" rx="1"/></svg>0427 318865</li>
      <li><svg class="icon" viewBox="0 0 12 12" aria-hidden="true"><path d="M2.5 1 L5 3.5 L3.8 5 Q5 7.5 7 8.2 L8.5 7 L11 9.5 L9.5 11 Q4 10.5 1 3 Z"/></svg>03 50718 962</li>
      <li><svg class="icon" viewBox="0 0 12 12" aria-hidden="true"><rect x="1" y="4" width="10" height="6" rx="1"/><rect x="3" y="1" width="6" height="3"/></svg>03 50718 415</li>
      <li><svg class="icon" viewBox="0 0 12 12" aria-hidden="true"><path d="M1 2.5 H11 V9.5 H1 Z M1 2.5 L6 6.5 L11 2.5" stroke="#fff" stroke-width=".8"/></svg>email DennisO@tbvbuild.net.au</li>
      <li><svg class="icon" viewBox="0 0 12 12" aria-hidden="true"><circle cx="6" cy="6" r="5"/></svg>www.tallbrookhomes.net.au</li>
    </ul>

    <div class="base-band"></div>
  </section>

</body>
</html>
```